TRUCKING/TRANSPORTATION COMPANY BUSINESS CARD.

We need a business card design for our trucking company based in Cedarview, OK.
It will be a double sided design.
FRONT SIDE:
We need a good looking logo with a tagline. The tagline should match the type of business.
COMPANY NAME: RW HAULAGE LLC
BACK SIDE:
The following information should be displayed on the back of the card.
Office: 555.274.0918
Mailing: 482 W. Birch Ave.
Cedarview, OK 30917
Email: rwhaulllc@mailbox-example.net
FRONT SIDE:
BACK SIDE:
Office: 555.274.0918
Mailing: 482 W. Birch Ave.
Cedarview, OK 30917

```html
<!DOCTYPE html>
<html lang="en">
<head>
<meta charset="utf-8">
<title>RW Haulage LLC — Business Card</title>
<link rel="stylesheet" href="https://fonts.googleapis.com/css2?family=Quicksand:wght@300;500;700&display=swap">
<style>
  :root {
    --page-bg: #e9e6e1;
    --card-black: #0b0b0c;
    --card-glow: #2a2a2c;
    --panel-grey: #c9c9c9;
    --ink-light: #d6d6d6;
    --ink-mid: #9a9a9a;
    --ink-dark: #1a1a1a;
    --rule: #6f6f6f;
  }
  * { margin: 0; padding: 0; box-sizing: border-box; }
  html, body { width: 1200px; height: 1000px; overflow: hidden; }
  body {
    background: var(--page-bg);
    font-family: "Quicksand", sans-serif;
    display: flex;
    flex-direction: column;
    align-items: center;
    justify-content: center;
    gap: 60px;
  }
  .card {
    width: 700px;
    height: 400px;
    position: relative;
    overflow: hidden;
    background: radial-gradient(ellipse at 50% 40%, var(--card-glow) 0%, var(--card-black) 65%);
    box-shadow: 0 10px 30px rgba(0,0,0,.25);
  }
  /* Front */
  .card-front {
    display: flex;
    flex-direction: column;
    align-items: center;
    justify-content: center;
    gap: 22px;
  }
  .brand-name {
    font-weight: 700;
    font-size: 38px;
    letter-spacing: 3px;
    color: var(--ink-light);
  }
  .tagline {
    font-weight: 700;
    font-size: 15px;
    letter-spacing: 5px;
    color: var(--ink-light);
  }
  /* Back */
  .card-back { display: flex; }
  .back-edge { width: 80px; flex: none; }
  .brand-panel {
    width: 210px;
    flex: none;
    background: var(--panel-grey);
    display: flex;
    align-items: center;
    justify-content: center;
  }
  .brand-panel .brand-name {
    color: var(--ink-dark);
    font-size: 30px;
    writing-mode: vertical-rl;
    transform: rotate(180deg);
    white-space: nowrap;
  }
  .contact-list {
    list-style: none;
    flex: 1;
    padding: 48px 30px 0 36px;
  }
  .contact-item {
    display: flex;
    align-items: center;
    gap: 20px;
    padding: 22px 0;
    border-bottom: 1px solid var(--rule);
    color: var(--ink-light);
    font-weight: 300;
    font-size: 21px;
    line-height: 1.3;
  }
  .contact-item:last-child { border-bottom: none; }
  .contact-item.email { font-size: 17px; white-space: nowrap; }
  .icon { width: 34px; height: 34px; flex: none; }
</style>
</head>
<body>
  <section class="card card-front" aria-label="Card front">
    <div class="brand-name">RW HAULAGE LLC</div>
    <div class="tagline">YOUR TAGLINE SLOGAN HERE</div>
  </section>

  <section class="card card-back" aria-label="Card back">
    <div class="back-edge"></div>
    <div class="brand-panel">
      <div class="brand-name">RW HAULAGE LLC</div>
    </div>
    <ul class="contact-list">
      <li class="contact-item phone">
        <svg class="icon" viewBox="0 0 34 34" aria-hidden="true">
          <circle cx="17" cy="17" r="16" fill="var(--ink-mid)"/>
          <path d="M12 9c1-1 2 0 3 2l1 2c0 1-1 2-1 2 1 2 2 3 4 4 0 0 1-1 2-1l2 1c2 1 3 2 2 3l-1 1c-2 2-7 0-10-3s-5-8-3-10z" fill="var(--ink-dark)"/>
        </svg>
        <span>555.274.0918</span>
      </li>
      <li class="contact-item email">
        <svg class="icon" viewBox="0 0 34 34" aria-hidden="true">
          <circle cx="17" cy="17" r="16" fill="var(--ink-mid)"/>
          <rect x="9" y="11" width="16" height="12" fill="var(--ink-dark)"/>
          <path d="M9 11l8 7 8-7" fill="none" stroke="var(--ink-mid)" stroke-width="1.5"/>
        </svg>
        <span>rwhaulllc@mailbox-example.net</span>
      </li>
      <li class="contact-item address">
        <svg class="icon" viewBox="0 0 34 34" aria-hidden="true">
          <circle cx="17" cy="17" r="16" fill="var(--ink-mid)"/>
          <path d="M17 8a6 6 0 0 1 6 6c0 5-6 12-6 12s-6-7-6-12a6 6 0 0 1 6-6z" fill="var(--ink-dark)"/>
          <circle cx="17" cy="14" r="2.2" fill="var(--ink-mid)"/>
        </svg>
        <span>482 W. Birch Ave. Cedarview,<br>OK 30917</span>
      </li>
    </ul>
  </section>
</body>
</html>
```